I'm an electrician and the name of my company is called Brisk 'N' Bright Electrical. I require a professional business card that speaks to my clients, I also need it to be innovative and modern. We do maintenance & service work for domestic and commercial premises.

Industry/Entity Type

Electrical

Contact Information for Business Card

Must have the name of my company Brisk 'N' Bright Electrical, my name Darren Kolovos and my contact details 0427 381 592 and company email address Brisknbrightelectrical@mailvane.com and/or website Brisknbrightelectrical.com.au

Logo Text

Brisk 'N' Bright Electrical (If possible)

Colors
33a6d7
0592cd
3176b5

```html
<!DOCTYPE html>
<html lang="en">
<head>
<meta charset="UTF-8">
<title>Brisk 'N' Bright Electrical – Business Card</title>
<link href="https://fonts.googleapis.com/css2?family=Exo+2:ital,wght@0,400;0,500;0,600;0,700;1,700&display=swap" rel="stylesheet">
<style>
  :root {
    --backdrop: #242424;
    --card: #141414;
    --silver: #c9c9c9;
    --white: #f2f2f2;
    --blue: #3176b5;
    --yellow: #e2d420;
    --divider: #d8d8d8;
  }
  * { margin: 0; padding: 0; box-sizing: border-box; }
  html, body {
    width: 1200px; height: 1200px; overflow: hidden;
    background: var(--backdrop);
    font-family: "Exo 2", sans-serif;
  }
  .canvas {
    position: relative; width: 1200px; height: 1200px;
  }
  .card {
    position: absolute; left: 160px;
    width: 880px; height: 500px;
    background: var(--card);
    border-radius: 24px;
    box-shadow: 0 16px 40px rgba(0,0,0,.45);
  }
  .card--front { top: 70px; }
  .card--back { top: 630px; }

  /* Front */
  .front-brand {
    position: absolute; top: 50%; left: 50%;
    transform: translate(-50%, -50%);
    display: flex; align-items: center; gap: 26px;
  }
  .front-brand__square {
    width: 70px; height: 70px;
    border: 7px solid var(--silver);
  }
  .front-brand__name {
    color: var(--silver);
    font-weight: 600; font-size: 40px; line-height: 1.05;
    letter-spacing: 3px; text-transform: uppercase;
  }

  /* Back */
  .back-brand {
    position: absolute; left: 70px; top: 150px;
    width: 190px; height: 170px;
    display: flex; flex-direction: column; justify-content: center; gap: 14px;
  }
  .back-brand__square {
    width: 46px; height: 46px; background: var(--blue);
  }
  .back-brand__name {
    color: var(--white); font-weight: 600; font-size: 24px;
    line-height: 1.1; text-transform: uppercase; letter-spacing: 1px;
  }
  .divider {
    position: absolute; left: 290px; top: 140px;
    width: 2px; height: 190px; background: var(--divider);
    transform: rotate(8deg);
  }
  .person {
    position: absolute; left: 340px; top: 150px;
  }
  .person__name {
    font-size: 32px; font-weight: 500; letter-spacing: 2px;
    text-transform: uppercase; line-height: 1;
  }
  .person__first { color: var(--blue); }
  .person__last { color: var(--yellow); }
  .person__role {
    color: var(--white); font-size: 22px; letter-spacing: 2px;
    text-transform: uppercase; margin-top: 4px;
  }
  .contacts {
    list-style: none; margin-top: 18px;
  }
  .contacts li {
    display: flex; align-items: center; gap: 14px;
    color: var(--white); font-size: 21px; letter-spacing: 1px;
    height: 32px;
  }
  .contacts svg { width: 20px; height: 20px; flex: none; }
  .tagline {
    position: absolute; left: 0; right: 0; bottom: 56px;
    text-align: center;
    color: var(--yellow); font-weight: 700; font-style: italic;
    font-size: 22px; letter-spacing: 1px; text-transform: uppercase;
  }
</style>
</head>
<body>
<main class="canvas">

  <section class="card card--front" aria-label="Card front">
    <div class="front-brand">
      <div class="front-brand__square"></div>
      <div class="front-brand__name">Brisk 'N' Bright<br>Electrical</div>
    </div>
  </section>

  <section class="card card--back" aria-label="Card back">
    <div class="back-brand">
      <div class="back-brand__square"></div>
      <div class="back-brand__name">Brisk 'N' Bright Electrical</div>
    </div>

    <div class="divider"></div>

    <div class="person">
      <p class="person__name"><span class="person__first">Darren</span> <span class="person__last">Kolovos</span></p>
      <p class="person__role">Electrician</p>
      <ul class="contacts">
        <li>
          <svg viewBox="0 0 24 24" aria-hidden="true"><path fill="var(--yellow)" d="M6.6 10.8a15.1 15.1 0 0 0 6.6 6.6l2.2-2.2a1 1 0 0 1 1-.25 11.4 11.4 0 0 0 3.6.57 1 1 0 0 1 1 1V20a1 1 0 0 1-1 1A17 17 0 0 1 3 4a1 1 0 0 1 1-1h3.5a1 1 0 0 1 1 1c0 1.25.2 2.45.57 3.57a1 1 0 0 1-.25 1z"/></svg>
          0427 381 592
        </li>
        <li>
          <svg viewBox="0 0 24 24" aria-hidden="true"><rect x="2" y="5" width="20" height="14" fill="var(--yellow)"/><path d="M2 5l10 8 10-8" fill="none" stroke="var(--card)" stroke-width="1.8"/></svg>
          Brisknbrightelectrical@mailvane.com
        </li>
        <li>
          <svg viewBox="0 0 24 24" aria-hidden="true"><g fill="none" stroke="var(--yellow)" stroke-width="1.6"><circle cx="12" cy="12" r="9"/><ellipse cx="12" cy="12" rx="4" ry="9"/><path d="M3 12h18M4.5 7.5h15M4.5 16.5h15"/></g></svg>
          Brisknbrightelectrical.com.au
        </li>
      </ul>
    </div>

    <p class="tagline">Maintenance &amp; service work for domestic and commercial premises</p>
  </section>

</main>
</body>
</html>
```